Need a graphic design to promote our new online learning system

We are seeking a graphic design to be promoted on social media to promote our new Online earning Management system (OKRU-LMS). The purpose is to make the design attractive and informative for parents and students so they can enrol at our School.

It must state the benefits of the OKRU-LMS. Colourful but not too busy.

```html
<!DOCTYPE html>
<html lang="en">
<head>
<meta charset="utf-8">
<title>OKRU-LMS Launch Flyer</title>
<link rel="stylesheet" href="https://fonts.googleapis.com/css2?family=Montserrat:ital,wght@0,400;0,600;0,700;0,800;1,700;1,800&family=Open+Sans:ital,wght@1,600&display=swap">
<style>
  :root {
    --navy: #034694;
    --sky: #40b4e5;
    --ink: #333333;
    --body: #3a3a3a;
    --white: #ffffff;
    --page: #ffffff;
  }
  * { margin: 0; padding: 0; box-sizing: border-box; }
  html, body {
    width: 986px; height: 1200px; overflow: hidden;
    background: var(--page);
    font-family: "Montserrat", sans-serif;
  }
  .flyer {
    position: absolute; left: 88px; top: 28px;
    width: 809px; height: 1144px;
    background: var(--white);
    box-shadow: 0 0 8px rgba(0,0,0,0.18);
    overflow: hidden;
  }
  .corner-flag { position: absolute; left: 0; top: 0; }
  .teaser {
    position: absolute; left: 20px; top: 38px;
    color: var(--white); font-weight: 800; font-size: 16px; line-height: 19px;
  }
  .teaser-title { display: block; font-size: 32px; line-height: 38px; margin-top: 2px; }

  .brand { position: absolute; left: 397px; top: 24px; display: flex; align-items: flex-start; gap: 14px; }
  .brand-square { width: 60px; height: 60px; background: var(--navy); margin-top: 4px; }
  .brand-name {
    color: var(--navy); font-weight: 600; font-size: 22px; line-height: 26px; letter-spacing: 1.5px;
  }
  .school-id {
    position: absolute; left: 471px; top: 98px; width: 290px; text-align: center;
    color: var(--navy); font-weight: 600; font-size: 19px;
    border-top: 2px solid #8a8a9a; padding-top: 2px;
  }

  .campus-photo {
    position: absolute; left: 0; top: 145px; width: 809px; height: 385px;
    background: linear-gradient(180deg, #ecdfe2 0%, #f3f1f0 40%, #e4e6e3 70%, #c9c7c3 100%);
  }
  .announcement {
    position: absolute; left: 30px; top: 200px; width: 770px;
    color: var(--ink); font-weight: 700; font-size: 24px; line-height: 42px;
  }
  .announcement em { font-style: italic; }
  .slogan {
    position: absolute; left: 30px; top: 338px;
    color: var(--navy); font-weight: 800; font-style: italic; font-size: 53px; line-height: 56px;
  }

  .divider { position: absolute; left: 0; top: 530px; }
  .access-band {
    position: absolute; left: 0; top: 556px; width: 809px; height: 102px;
    background: var(--sky); color: var(--white);
    padding: 10px 0 0 27px; font-size: 18px; line-height: 33px; font-weight: 400;
  }
  .access-band strong { font-size: 32px; font-weight: 600; }

  .intro {
    position: absolute; left: 27px; top: 664px; width: 770px;
    color: var(--ink); font-weight: 800; font-size: 16.5px; line-height: 30px;
  }
  .learner-photo {
    position: absolute; left: 20px; top: 764px; width: 332px; height: 267px;
    background: linear-gradient(135deg, #e9e4df 0%, #d8d2cc 45%, #a9c9c9 75%, #6fb9c4 100%);
  }
  .benefits { position: absolute; left: 366px; top: 772px; width: 440px; list-style: none; }
  .benefits li {
    position: relative; padding-left: 22px; margin-bottom: 10px;
    color: var(--body); font-size: 17px; line-height: 24px;
  }
  .benefits li svg { position: absolute; left: 0; top: 6px; }

  .footer {
    position: absolute; left: 0; top: 1058px; width: 809px; height: 86px;
    background: var(--navy); color: var(--white);
  }
  .footer-label {
    position: absolute; left: 53px; top: 12px;
    font-weight: 800; font-style: italic; font-size: 27px;
  }
  .footer-web { position: absolute; left: 56px; top: 48px; font-size: 24px; font-weight: 400; }
  .footer-phone {
    position: absolute; left: 490px; top: 10px;
    font-family: "Open Sans", sans-serif; font-style: italic; font-weight: 600; font-size: 37px; letter-spacing: 2px;
  }
</style>
</head>
<body>
<main class="flyer">
  <svg class="corner-flag" width="360" height="145" viewBox="0 0 360 145" aria-hidden="true">
    <polygon points="0,0 165,0 352,145 0,145" fill="var(--navy)"/>
  </svg>
  <p class="teaser">HAVE YOU HEARD<br>ABOUT THE........<span class="teaser-title">OKRU-LMS???</span></p>

  <div class="brand">
    <span class="brand-square"></span>
    <p class="brand-name">NORTHFIELD<br>ACADEMY OF KELVAR</p>
  </div>
  <p class="school-id">School ID 517342</p>

  <div class="campus-photo" role="img" aria-label="Faded photo of the school campus building and courtyard"></div>
  <p class="announcement">THE <em>NORTHFIELD ACADEMY OF KELVAR</em> IS PLEASED TO ANNOUNCE THE OFFICIAL LAUNCH OUR ONLINE STUDENT LEARNING MANAGEMENT SYSTEM (OKRU-LMS).</p>
  <p class="slogan">“BE A PART OF<br>SOMTHING BIG”</p>

  <svg class="divider" width="809" height="26" viewBox="0 0 809 26" aria-hidden="true">
    <polygon points="0,0 494,0 470,26 0,26" fill="var(--navy)"/>
  </svg>
  <div class="access-band">
    Students will have access to their OKRU-LMS account <strong>24 hours</strong> a day,<br>
    <strong>7 days</strong> aweek, <strong>365 days</strong> of the year.
  </div>

  <p class="intro">The OKRU-LMS is an online student learning, assessment and grading platform where Northfield students can access their learning material, modules, learning videos, reading materials, exams, asssessment and gradings.</p>

  <div class="learner-photo" role="img" aria-label="Photo of a child with headphones joining an online class on a desktop computer"></div>
  <ul class="benefits">
    <li><svg width="15" height="12" viewBox="0 0 15 12" aria-hidden="true"><polygon points="0,0 15,6 0,12 4,6" fill="var(--navy)"/></svg>It is available on any Smart device, from any city in any country.</li>
    <li><svg width="15" height="12" viewBox="0 0 15 12" aria-hidden="true"><polygon points="0,0 15,6 0,12 4,6" fill="var(--navy)"/></svg>It offers all learning subjects for all year levels (Kindergarten to year 12)</li>
    <li><svg width="15" height="12" viewBox="0 0 15 12" aria-hidden="true"><polygon points="0,0 15,6 0,12 4,6" fill="var(--navy)"/></svg>It offers 144 Learning subjects, all learning modules</li>
    <li><svg width="15" height="12" viewBox="0 0 15 12" aria-hidden="true"><polygon points="0,0 15,6 0,12 4,6" fill="var(--navy)"/></svg>It offers students exams, quizzes, assignments, essays and much more.</li>
    <li><svg width="15" height="12" viewBox="0 0 15 12" aria-hidden="true"><polygon points="0,0 15,6 0,12 4,6" fill="var(--navy)"/></svg>It is user-friendly and extremely versatile.</li>
  </ul>

  <footer class="footer">
    <p class="footer-label">To enrol online visit or call:</p>
    <p class="footer-web">northfield-kelvar.com.au</p>
    <p class="footer-phone">0917 555 0184</p>
  </footer>
</main>
</body>
</html>
```